Business Card Upgrade

I have designed our business card using our new logo. I think it needs imporovements. We used to have two cards for our business. One card was for our software business, and the other was for our consulting business. We are now in the process of combining our websites, marketing, name, and a new logo.

Our goal is to have a really sharp professional logo. One reason I designed the card the way I did was that our Titles are sometimes long, and by separating the person's name and title, it shows up very well and the title can be adjusted no matter how long it is. Sometimes the title can be 4 or 5 words or more.

We really like our logo on black as it shows up very nice. Our PMS colors are as follows: 368C and 459C.

The Designer that will be working with us will need to deliver the following:

The front and back of the Business Card Design will need to be delivered in a high quality JPEG, and
The front and back of the Business Card Design in Illustrator Format .ai
Any fonts will need to be sent to us if they are not standard and are required to open the Illustrator file correctly.

To help us get a good idea of the card with a title, please use the title: " Director of Software Development "

NOTE: The chosen designer will be selected to design our new letterhead within 2 weeks from the closing of this contest.

To help us make sure the card design works with longer titles, please use the followign job title on the card:  

"Director of Software and Product Development"

 

ALL DESIGNERS:

1. I appreciate the different angles you are showing the cards, but please be sure and always show the direct view, so I can see the layout and what the person I hand the card will see.

2. Please do not use white.  Please use off white as I don't care for white cards and they get dirty easy and do not represent the designs well.

Dear Designers,

Please provide samples straight one as a viewer of the card will see.  Some of the angles that are presented make it impossible to tell how everything fits, and sometimes even makes areas look skewed. So, please provide a straight sample view.

Pinnacle 400 company executives such as Vice Presidents, and Directors

Software

• Professional looking Card.

Our customers are Directors, Vice Presidents, and Presidents of companies as large as Pinnacle 400 companies. The card needs to get attention wile still looking professional.

Delivery of the finished product in Illustrator Format with any fonts needed to edit the text or open the file.

The card will be a heavy stock with a soft touch coating for that silk feel.

```html
<!DOCTYPE html>
<html lang="en">
<head>
<meta charset="utf-8">
<title>Harborline Trade – Business Card</title>
<link rel="stylesheet" href="https://fonts.googleapis.com/css2?family=Jost:wght@400;500;600;700&family=Oswald:wght@600&display=swap">
<style>
  :root {
    --page: #ffffff;
    --card: #000000;
    --green: #7ab929;
    --ring: #6fd14a;
    --ink: #ffffff;
    --tag: #eef3f7;
    --cream: #f1ea9c;
    --circle-text: #e4f5d8;
  }
  html, body {
    margin: 0;
    width: 1116px;
    height: 1200px;
    overflow: hidden;
    background: var(--page);
  }
  .canvas { position: relative; width: 1116px; height: 1200px; }
  .card {
    position: absolute;
    background: var(--card);
    overflow: hidden;
    font-family: "Jost", sans-serif;
  }
  .card--front { left: 154px; top: 51px; width: 807px; height: 533px; }
  .card--back  { left: 159px; top: 613px; width: 806px; height: 533px; }

  .front__band {
    position: absolute; left: 0; top: 0; width: 100%; height: 296px;
    background:
      radial-gradient(ellipse 75% 55% at 50% 100%, rgba(200,225,240,.85) 0%, rgba(90,140,185,.6) 35%, rgba(20,40,70,.25) 65%, transparent 80%),
      #000;
  }
  .brand {
    position: absolute; left: 0; right: 0; top: 86px;
    text-align: center;
    color: var(--green);
    font-weight: 700; font-size: 64px; letter-spacing: 9px;
    line-height: 1;
  }
  .brand__sub {
    position: absolute; left: 0; right: 0; top: 176px;
    text-align: center; color: var(--green);
    font-weight: 700; font-size: 28px; letter-spacing: 20px; line-height: 1;
  }
  .tagline {
    position: absolute; left: 0; right: 0; top: 248px;
    text-align: center; color: var(--tag);
    font-family: "Oswald", sans-serif; font-weight: 600;
    font-size: 21px; letter-spacing: .3px; transform: scaleX(.85);
    white-space: nowrap;
  }
  .person { position: absolute; left: 0; right: 0; top: 318px; text-align: center; }
  .person__name { color: var(--ink); font-size: 41px; font-weight: 500; margin: 0; line-height: 1.2; }
  .person__title { color: var(--green); font-size: 28px; font-weight: 500; margin: 4px 0 0; }
  .person__contact { color: var(--ink); font-size: 25px; margin: 14px 0 0; line-height: 1.33; }

  .back__map { position: absolute; inset: 0; }
  .back__art { position: absolute; inset: 0; }
  .back__url {
    position: absolute; left: 0; right: 0; top: 396px;
    text-align: center; white-space: nowrap;
    font-weight: 700; line-height: 1;
  }
  .back__url .small { color: var(--cream); font-size: 36px; }
  .back__url .big { color: var(--green); font-size: 80px; letter-spacing: 1px; }

  .service-label { font-family: "Jost", sans-serif; font-weight: 600; font-size: 22px; fill: var(--ink); letter-spacing: 1px; }
  .service-list { font-family: "Jost", sans-serif; font-weight: 600; font-size: 10.5px; fill: var(--circle-text); }
</style>
</head>
<body>
<div class="canvas">

  <section class="card card--front">
    <div class="front__band"></div>
    <div class="brand">HARBORLINE</div>
    <div class="brand__sub">TRADE</div>
    <div class="tagline">ONE PARTNER WITH THE DEPTH TO DELIVER EVERY TRADE ZONE SERVICE</div>
    <div class="person">
      <p class="person__name">Daniel Marsh</p>
      <p class="person__title">Director of Software &amp; Product Development</p>
      <p class="person__contact">418 Harbor View Lane, 555.014.2290 (Direct)<br>Bayport, Alabama 36690, dmarsh@harborline.com</p>
    </div>
  </section>

  <section class="card card--back">
    <svg class="back__map" width="806" height="533" role="img" aria-label="World map with radiating green light lines">
      <defs>
        <radialGradient id="mapGlow" cx="50%" cy="45%" r="65%">
          <stop offset="0" stop-color="#1f5a2a"/>
          <stop offset=".5" stop-color="#0d2e16"/>
          <stop offset="1" stop-color="#020603"/>
        </radialGradient>
      </defs>
      <rect width="806" height="533" fill="url(#mapGlow)"/>
    </svg>

    <svg class="back__art" width="806" height="533" viewBox="0 0 806 533">
      <defs>
        <path id="arc1" d="M 14 210 A 90 90 0 0 1 194 210"/>
        <path id="arc2" d="M 210 210 A 90 90 0 0 1 390 210"/>
        <path id="arc3" d="M 409 210 A 90 90 0 0 1 589 210"/>
        <path id="arc4" d="M 604 210 A 90 90 0 0 1 784 210"/>
        <radialGradient id="disc" cx="50%" cy="45%" r="55%">
          <stop offset="0" stop-color="#0d3a14"/>
          <stop offset="1" stop-color="#021005"/>
        </radialGradient>
      </defs>

      <g class="service service--consulting">
        <text class="service-label"><textPath href="#arc1" startOffset="50%" text-anchor="middle">CONSULTING</textPath></text>
        <circle cx="104" cy="210" r="74" fill="url(#disc)" stroke="var(--ring)" stroke-width="5"/>
        <text class="service-list" text-anchor="middle" x="104">
          <tspan y="168">Zone Activation</tspan><tspan x="104" y="182">Subzone Applications</tspan><tspan x="104" y="196">Benefit Analysis</tspan><tspan x="104" y="210">Site Expansions</tspan><tspan x="104" y="224">Boundary Changes</tspan><tspan x="104" y="238">Compliance Review</tspan><tspan x="104" y="252">Staff Training</tspan>
        </text>
      </g>

      <g class="service service--software">
        <text class="service-label"><textPath href="#arc2" startOffset="50%" text-anchor="middle">SOFTWARE</textPath></text>
        <circle cx="300" cy="210" r="74" fill="url(#disc)" stroke="var(--ring)" stroke-width="5"/>
        <text class="service-list" text-anchor="middle" x="300" style="font-size:14px">
          <tspan y="175">ZoneTrack</tspan><tspan x="300" y="193">ClassifyPro</tspan><tspan x="300" y="211">ISF Manager</tspan><tspan x="300" y="229">Zone Ledger</tspan><tspan x="300" y="247">Audit Suite</tspan><tspan x="300" y="262" style="font-size:11px">Entry Portal</tspan>
        </text>
      </g>

      <g class="service service--operations">
        <text class="service-label"><textPath href="#arc3" startOffset="50%" text-anchor="middle">OPERATIONS</textPath></text>
        <circle cx="499" cy="210" r="74" fill="url(#disc)" stroke="var(--ring)" stroke-width="5"/>
        <text class="service-list" text-anchor="middle" x="499">
          <tspan y="168">Zone Operations</tspan><tspan x="499" y="182">Regulatory Management</tspan><tspan x="499" y="196">Weekly Entry Filing</tspan><tspan x="499" y="210">Managed Services</tspan><tspan x="499" y="224">Annual Reports</tspan><tspan x="499" y="238">Procedures Manual</tspan><tspan x="499" y="252">Security Updates</tspan>
        </text>
      </g>

      <g class="service service--administration">
        <text class="service-label"><textPath href="#arc4" startOffset="50%" text-anchor="middle">ADMINISTRATION</textPath></text>
        <circle cx="694" cy="210" r="74" fill="url(#disc)" stroke="var(--ring)" stroke-width="5"/>
        <text class="service-list" text-anchor="middle" x="694">
          <tspan y="168">Project Oversight</tspan><tspan x="694" y="182">Zone Schedules</tspan><tspan x="694" y="196">Grantee Administration</tspan><tspan x="694" y="210">Operator Agreements</tspan><tspan x="694" y="224">Grantee Reporting</tspan><tspan x="694" y="238">Fee Schedules</tspan><tspan x="694" y="252">Zone Marketing</tspan>
        </text>
      </g>
    </svg>

    <div class="back__url"><span class="small">www.</span><span class="big">HARBORLINE</span><span class="small">.com</span></div>
  </section>

</div>
</body>
</html>
```